Tomás Rivera (Business Card)

Hi designers, in this work, I'm looking for an sophisticated stylish, elegant and proffesional personal card. We have a laboratory of pathology automated, with equipments high quality.
In this web the designers, have created my business logo, the name is "Tomás Rivera"
In our lab, we principal work is to prepare the biopsies for further diagnostic of diseases like cancer, tumors, etc.
I need that the first face, only having my complete logo (Rm Tomás Rivera, Laboratorio de procesamiento Histologico)
The overleaf, could repeat the same logo, like water logo.
In this face, I need to say: My full data:

Técnico en Anatomía Patológica
Tomás Rivera Ibarra M.P 47203
Av. Paredes Luján 418 - 2do piso - Instituto Marbel.
Córdoba, Argentina
(0351) 154820937
rivera.tomas@correolab.example

with respect the colors of card, use your imagination, the original logo color is violet, I haven't chosen a color base for the card.

attached pictures are examples of cards I like your DESIGN.
Attached too, the original logo to my company.

the size of card are:
horizontal: 9cm
vertical: 5,5cm

any question that you have, not doubt to question me,
Hand to work!

Industry/Entity Type

Laboratory

Requirements
Must have
• designers sophisticated, not simples, like show the images attached

```html
<!DOCTYPE html>
<html lang="es">
<head>
<meta charset="utf-8">
<title>Tomás Rivera – Tarjeta personal</title>
<link href="https://fonts.googleapis.com/css2?family=Questrial&display=swap" rel="stylesheet">
<style>
  :root {
    --page-bg: #d2dadd;
    --card-white: #ffffff;
    --violet: #5a1a8a;
    --violet-deep: #3a0a5c;
    --violet-light: #6e2aa0;
    --ink: #1f1f1f;
    --frame-grey: #e3e3e3;
    --white: #ffffff;
  }
  * { margin: 0; padding: 0; box-sizing: border-box; }
  html, body { width: 1200px; height: 1012px; overflow: hidden; }
  body {
    background: var(--page-bg);
    font-family: "Questrial", sans-serif;
    position: relative;
  }
  .card {
    position: absolute;
    border-radius: 28px;
    overflow: hidden;
  }

  /* Front: contact side */
  .card-front {
    left: 316px; top: 155px; width: 591px; height: 335px;
    background: var(--card-white);
  }
  .violet-band {
    position: absolute; left: 101px; top: 0; width: 89px; height: 100%;
    background: linear-gradient(180deg, var(--violet-deep) 0%, var(--violet) 55%, var(--violet-light) 100%);
  }
  .name-panel {
    position: absolute; left: 8px; top: 30px; width: 196px; height: 168px;
    background: var(--card-white);
    border: 3px solid var(--frame-grey);
    border-radius: 10px;
    display: flex; align-items: center; justify-content: center;
  }
  .holder-name {
    color: var(--violet);
    font-size: 15.5px;
    font-weight: 700;
    white-space: nowrap;
  }
  .contact {
    position: absolute; left: 271px; top: 42px;
    color: var(--ink);
    font-size: 14px;
    line-height: 18px;
  }
  .profession { font-style: italic; }
  .profession strong { font-weight: 700; }
  .address { margin-top: 28px; }
  .contact-line {
    display: flex; align-items: center; gap: 10px;
    margin-top: 5px;
  }
  .contact-line svg { flex: none; }
  .front-brand {
    position: absolute; left: 271px; top: 236px; width: 250px;
    text-align: center;
    color: var(--violet);
    font-size: 20px;
    letter-spacing: 4px;
  }

  /* Back: brand side */
  .card-back {
    left: 313px; top: 522px; width: 592px; height: 336px;
    background: radial-gradient(ellipse at 50% 30%, var(--violet-light) 0%, var(--violet) 45%, var(--violet-deep) 100%);
    display: flex; align-items: center; justify-content: center;
  }
  .back-brand {
    color: var(--white);
    font-size: 40px;
    letter-spacing: 10px;
    white-space: nowrap;
  }
</style>
</head>
<body>

  <section class="card card-front" aria-label="Frente de la tarjeta">
    <div class="violet-band"></div>
    <div class="name-panel">
      <p class="holder-name">Tomás Rivera Ibarra</p>
    </div>

    <div class="contact">
      <p class="profession">Profession (Pathology Technician)<br><strong>Técnico en Anatomía Patológica</strong></p>
      <p class="address">Av. Paredes Luján 418 - 2do piso -<br>Instituto Marbel. Cordoba, Argentina</p>
      <p class="contact-line">
        <svg width="11" height="17" viewBox="0 0 11 17" aria-hidden="true">
          <rect x="1" y="1" width="9" height="15" rx="1.5" fill="none" stroke="#1f1f1f" stroke-width="1.6"/>
          <line x1="4" y1="13.5" x2="7" y2="13.5" stroke="#1f1f1f" stroke-width="1.2"/>
        </svg>
        (0351) 154820937
      </p>
      <p class="contact-line">
        <svg width="18" height="12" viewBox="0 0 18 12" aria-hidden="true">
          <rect x="0.5" y="0.5" width="17" height="11" fill="#1f1f1f"/>
          <polyline points="1,1 9,7 17,1" fill="none" stroke="#ffffff" stroke-width="1.2"/>
        </svg>
        rivera.tomas@correolab.example
      </p>
    </div>

    <p class="front-brand">Tomás Rivera</p>
  </section>

  <section class="card card-back" aria-label="Dorso de la tarjeta">
    <p class="back-brand">Tomás Rivera</p>
  </section>

</body>
</html>
```